Kovrilex - presentation for a remote DBA team offering data platform management

We need a website design for wordpress site called Kovrilex.cz
We deliver remote database and data platform administration and development, oversee the database administrators, consult and train the personnel responsible for the database operations. The website should include several sections, home page with graphics elements supporting the name and service - remote dba work; blog section; service introduction and description, team introduction and description, download section for documents, presentations etc.

Target Market(s)

small and medium business companies requiring remote DBA service

Number of Pages Required

3 page

Font styles to use
Sans Serif

Colors

Designer to choose colors to be used in the design.

Requirements
Must have
• The website should have several sections to introduce the services, blog, team introduction, downloads

```html
<!DOCTYPE html>
<html lang="en">
<head>
<meta charset="utf-8">
<title>Kovrilex – Remote Database Administration</title>
<link rel="stylesheet" href="https://fonts.googleapis.com/css2?family=Lato:wght@400;700;900&family=Oswald:wght@400;500&display=swap">
<style>
:root{
  --blue:#2563c4;
  --blue-dark:#174a9c;
  --navy:#1b2a4a;
  --ink:#333a44;
  --muted:#6b7380;
  --light:#f1f2f4;
  --footer:#1f2023;
  --footer-text:#c9ccd2;
  --white:#ffffff;
}
*{box-sizing:border-box;margin:0;padding:0}
html,body{width:1200px;height:3844px;overflow:hidden;background:var(--white)}
body{font-family:'Lato',sans-serif;color:var(--ink)}
.page{position:relative;width:1200px;height:3844px;overflow:hidden}
.abs{position:absolute}
a{color:inherit;text-decoration:none}

/* header */
.topbar{left:0;top:0;width:1200px;height:52px;border-bottom:1px solid #e5e7ea}
.social{left:72px;top:16px;display:flex;gap:14px}
.social span{width:20px;height:20px;border-radius:50%;background:#4a4f57;display:block}
.contact-line{right:72px;top:14px;display:flex;gap:28px;font-size:15px;color:#555}
.contact-line span{display:flex;align-items:center;gap:8px}
.ico{width:22px;height:22px;border-radius:4px;background:var(--blue);display:inline-flex;align-items:center;justify-content:center}
.logo{left:72px;top:62px;font-family:'Oswald',sans-serif;font-weight:500;font-size:46px;letter-spacing:1px;color:#222;line-height:1}
.nav{right:72px;top:96px;display:flex;gap:30px;font-size:14px;font-weight:700;color:#333}
.nav a.active{color:var(--blue)}

/* hero */
.hero{left:0;top:160px;width:1200px;height:600px;background:linear-gradient(120deg,#0e1826 0%,#2d4a6e 45%,#8ea9c4 75%,#d7e3ee 100%)}
.hero-title{left:72px;top:566px;font-family:'Oswald',sans-serif;font-weight:500;font-size:44px;color:var(--white);letter-spacing:1px;line-height:1.2}
.hero-sub{left:72px;top:624px;width:450px;font-size:23px;line-height:1.25;color:var(--white)}

/* section heading */
.h2{left:0;width:1200px;text-align:center;font-weight:900;font-size:34px;color:var(--blue);letter-spacing:.5px}

/* welcome */
.welcome-text{left:148px;top:882px;width:904px;text-align:center;font-size:14px;line-height:1.7;color:var(--muted)}
.btn{left:526px;top:1004px;width:148px;height:42px;border-radius:21px;background:var(--navy);color:var(--white);font-size:14px;font-weight:700;display:flex;align-items:center;justify-content:center;letter-spacing:.5px}

/* services */
.services{left:0;top:1110px;width:1200px;height:470px}
.svc{width:300px;color:var(--white)}
.svc h3{font-size:24px;font-weight:700;margin-bottom:6px}
.svc p{font-size:13px;line-height:1.5;color:#dbe6f7}
.svc.left{text-align:right}
.svc-icon{width:72px;height:72px;border-radius:50%;background:var(--white);display:flex;align-items:center;justify-content:center}

/* team */
.member{width:240px;text-align:center}
.avatar{width:160px;height:160px;border-radius:50%;margin:0 auto;border:5px solid #e3e6ea;background:radial-gradient(circle at 50% 40%,#c9ccd1,#6b7280)}
.member h4{font-size:18px;font-weight:700;color:var(--blue-dark);margin-top:26px}
.member .role{font-size:12px;color:var(--muted);margin-top:2px}
.member p{font-size:13px;line-height:1.5;color:#444;margin-top:10px}
.member .more{display:block;font-size:13px;font-weight:700;color:var(--blue);margin-top:12px}
.arrow{width:30px;height:40px}

/* blog */
.wave{left:0;top:2040px;width:1200px;height:620px}
.post{width:336px}
.post .thumb{height:192px;border-radius:3px}
.post h4{font-size:20px;font-weight:900;color:var(--blue-dark);margin-top:22px}
.post p{font-size:13px;line-height:1.55;color:#555;margin-top:8px}
.post .more{display:block;font-size:13px;font-weight:700;color:var(--blue);margin-top:12px}

/* news */
.news-main{left:72px;top:2740px;width:520px;height:320px;background:linear-gradient(135deg,#2a4f7a,#3c7cc4 55%,#c6dcef)}
.news-main-cap{left:72px;top:2992px;width:520px;height:68px;background:rgba(20,30,48,.82);color:var(--white);padding:12px 18px;font-size:13px;line-height:1.5}
.news-item{left:608px;width:520px;height:92px;display:flex;gap:30px}
.news-item .thumb{width:160px;height:92px;flex:none;background:linear-gradient(135deg,#1c2e48,#4f7fae)}
.news-item h4{font-size:20px;font-weight:900;color:var(--blue-dark)}
.news-item p{font-size:13px;line-height:1.5;color:#555;margin-top:4px}
.news-item .more{font-size:13px;font-weight:700;color:var(--blue)}

/* testimonial */
.testi-band{left:0;top:3110px;width:1200px;height:420px;background:var(--light)}
.testi-card{left:160px;top:3156px;width:880px;height:330px;background:var(--white);box-shadow:0 4px 18px rgba(0,0,0,.12);text-align:center}
.testi-card h3{font-size:30px;font-weight:900;color:var(--blue);margin-top:26px}
.testi-card blockquote{font-size:14px;line-height:1.6;color:#555;font-style:italic;width:720px;margin:18px auto 0}
.testi-avatar{width:84px;height:84px;border-radius:50%;margin:20px auto 0;background:radial-gradient(circle at 50% 40%,#cfd2d6,#6b7280)}
.testi-card .name{font-size:14px;font-weight:900;color:var(--blue);margin-top:12px}

/* footer */
.footer{left:0;top:3590px;width:1200px;height:254px;background:var(--footer)}
.f-logo{left:72px;top:3644px;font-family:'Oswald',sans-serif;font-weight:400;font-size:50px;color:#e6e7ea;line-height:1;letter-spacing:1px}
.f-copy{left:72px;top:3716px;font-size:12px;line-height:1.6;color:var(--footer-text)}
.f-col{color:var(--footer-text)}
.f-col h5{font-size:15px;font-weight:900;color:var(--white);letter-spacing:.5px;margin-bottom:12px}
.f-col ul{list-style:none;font-size:13px;line-height:2}
.f-grid{display:flex;gap:34px}
.f-downloads li{display:flex;align-items:center;gap:8px}
.f-input{width:180px;height:34px;border-radius:17px;background:var(--white);color:#888;font-size:12px;padding:9px 16px}
.f-btn{width:86px;height:34px;border-radius:17px;background:var(--blue);color:var(--white);font-size:12px;font-weight:700;display:flex;align-items:center;justify-content:center}
</style>
</head>
<body>
<div class="page">

  <!-- header -->
  <div class="abs topbar"></div>
  <div class="abs social" aria-label="Social links"><span></span><span></span><span></span><span></span><span></span><span></span></div>
  <div class="abs contact-line">
    <span><i class="ico"><svg width="12" height="12" viewBox="0 0 24 24"><path fill="#fff" d="M6.6 10.8a15 15 0 0 0 6.6 6.6l2.2-2.2c.3-.3.7-.4 1-.2 1.1.4 2.3.6 3.6.6.6 0 1 .4 1 1V20c0 .6-.4 1-1 1A17 17 0 0 1 3 4c0-.6.4-1 1-1h3.5c.6 0 1 .4 1 1 0 1.3.2 2.5.6 3.6.1.3 0 .7-.2 1z"/></svg></i>555-014-2290</span>
    <span><i class="ico"><svg width="12" height="12" viewBox="0 0 24 24"><path fill="#fff" d="M2 5h20v14H2z"/><path fill="none" stroke="#2563c4" stroke-width="2" d="M2 5l10 8 10-8"/></svg></i>info@kovrilex.cz</span>
  </div>
  <div class="abs logo">KOVRILEX</div>
  <nav class="abs nav">
    <a class="active">HOME</a><a>ABOUT US</a><a>SERVICES</a><a>BLOG</a><a>CLIENTS</a><a>SOLUTIONS</a><a>CONTACT US</a>
  </nav>

  <!-- hero -->
  <div class="abs hero" role="img" aria-label="Photo of two engineers with a laptop in a server room"></div>
  <div class="abs hero-title">KOVRILEX</div>
  <div class="abs hero-sub">Suspendisse consectetur quam eu purus ultrices venenatis a non metus.</div>

  <!-- welcome -->
  <h2 class="abs h2" style="top:822px">WELCOME TO OUR WEBSITE</h2>
  <p class="abs welcome-text">Lorem ipsum dolor sit amet, consectetur adipiscing elit. Nunc ac aliquam risus, at tempus libero. Curabitur purus nisl, egestas nec posuere eget, malesuada sagittis eros. Morbi in sem vitae mauris dapibus auctor. Aenean vitae lacinia neque. Quisque volutpat dapibus mattis. Morbi egestas, mauris non congue commodo, luctus libero ultricies tellus, luctus fringilla ante urna sit amet.</p>
  <a class="abs btn">READ MORE</a>

  <!-- services -->
  <svg class="abs services" viewBox="0 0 1200 470" aria-hidden="true">
    <defs>
      <linearGradient id="svcGrad" x1="0" y1="0" x2="0" y2="1">
        <stop offset="0" stop-color="#2a6fd1"/><stop offset="1" stop-color="#1a4fa6"/>
      </linearGradient>
    </defs>
    <path d="M0 40 Q600 -30 1200 40 L1200 400 Q900 470 600 440 Q300 470 0 400 Z" fill="url(#svcGrad)"/>
    <path d="M0 40 Q600 -30 1200 40" fill="none" stroke="#5b93e0" stroke-width="3"/>
    <path d="M440 446 A160 150 0 0 1 760 446 Z" fill="#fff"/>
    <text x="600" y="430" text-anchor="middle" font-family="Oswald, sans-serif" font-size="46" font-weight="500" fill="#1b2a4a">KOVRILEX</text>
  </svg>
  <h2 class="abs h2" style="top:1180px;color:#fff;font-size:30px">OUR SERVICES</h2>

  <div class="abs svc left" style="left:230px;top:1276px"><h3>Remote Database</h3><p>Proin eu neque odio. Sed eleifend sodales diam a fermentum.</p></div>
  <div class="abs svc-icon" style="left:548px;top:1278px"><svg width="34" height="34" viewBox="0 0 24 24"><ellipse cx="12" cy="5" rx="8" ry="3" fill="#1b2a4a"/><path d="M4 5v14c0 1.7 3.6 3 8 3s8-1.3 8-3V5c0 1.7-3.6 3-8 3S4 6.7 4 5z" fill="#1b2a4a"/></svg></div>
  <div class="abs svc-icon" style="left:640px;top:1278px"><svg width="36" height="36" viewBox="0 0 24 24"><circle cx="8" cy="8" r="3.5" fill="#1b2a4a"/><circle cx="16" cy="8" r="3.5" fill="#1b2a4a"/><path d="M1 20c0-4 3-6 7-6s7 2 7 6zM14 14c4 0 9 1 9 6h-6" fill="#1b2a4a"/></svg></div>
  <div class="abs svc" style="left:740px;top:1276px"><h3>Consulting</h3><p>Proin eu neque odio. Sed eleifend sodales diam a fermentum.</p></div>

  <div class="abs svc left" style="left:160px;top:1384px"><h3>Data Administration</h3><p>Proin eu neque odio. Sed eleifend sodales diam a fermentum.</p></div>
  <div class="abs svc-icon" style="left:476px;top:1386px"><svg width="34" height="34" viewBox="0 0 24 24"><circle cx="12" cy="12" r="7" fill="none" stroke="#1b2a4a" stroke-width="4" stroke-dasharray="3 2.5"/><circle cx="12" cy="12" r="3" fill="#1b2a4a"/></svg></div>
  <div class="abs svc-icon" style="left:712px;top:1386px"><svg width="34" height="34" viewBox="0 0 24 24"><rect x="2" y="3" width="20" height="13" rx="1.5" fill="#1b2a4a"/><rect x="9" y="17" width="6" height="2" fill="#1b2a4a"/><rect x="6" y="19" width="12" height="2" fill="#1b2a4a"/></svg></div>
  <div class="abs svc" style="left:810px;top:1384px"><h3>Training</h3><p>Proin eu neque odio. Sed eleifend sodales diam a fermentum.</p></div>

  <!-- team -->
  <h2 class="abs h2" style="top:1586px">OUR TEAM</h2>
  <svg class="abs arrow" style="left:28px;top:1820px" viewBox="0 0 30 40" aria-hidden="true"><path d="M22 4 6 20l16 16" fill="none" stroke="#9aa0a8" stroke-width="4"/></svg>
  <svg class="abs arrow" style="left:1142px;top:1820px" viewBox="0 0 30 40" aria-hidden="true"><path d="M8 4l16 16L8 36" fill="none" stroke="#9aa0a8" stroke-width="4"/></svg>

  <div class="abs member" style="left:72px;top:1680px"><div class="avatar" role="img" aria-label="Portrait of a team member"></div><h4>Name Heading</h4><div class="role">Managing Director</div><p>Vivamus dignissim tellus vitae efficitur maximus. Praesent ac lacus et ligula ultricies.</p><a class="more">Read More</a></div>
  <div class="abs member" style="left:344px;top:1680px"><div class="avatar" role="img" aria-label="Portrait of a team member"></div><h4>Name Heading</h4><div class="role">Managing Director</div><p>Vivamus dignissim tellus vitae efficitur maximus. Praesent ac lacus et ligula ultricies.</p><a class="more">Read More</a></div>
  <div class="abs member" style="left:612px;top:1680px"><div class="avatar" role="img" aria-label="Portrait of a team member"></div><h4>Name Heading</h4><div class="role">Managing Director</div><p>Vivamus dignissim tellus vitae efficitur maximus. Praesent ac lacus et ligula ultricies.</p><a class="more">Read More</a></div>
  <div class="abs member" style="left:884px;top:1680px"><div class="avatar" role="img" aria-label="Portrait of a team member"></div><h4>Name Heading</h4><div class="role">Managing Director</div><p>Vivamus dignissim tellus vitae efficitur maximus. Praesent ac lacus et ligula ultricies.</p><a class="more">Read More</a></div>

  <!-- blog -->
  <svg class="abs wave" viewBox="0 0 1200 620" preserveAspectRatio="none" aria-hidden="true">
    <path d="M0 60 Q300 0 600 40 T1200 30 L1200 620 L0 620 Z" fill="#f1f2f4"/>
  </svg>
  <h2 class="abs h2" style="top:2140px">BLOG POSTS</h2>
  <div class="abs post" style="left:72px;top:2220px"><div class="thumb" role="img" aria-label="Illustration of data charts on a laptop" style="background:linear-gradient(135deg,#1f6fc8,#58a4e8)"></div><h4>LOREM IPSUM DOLOR SIT AMET</h4><p>Consectetur adipiscing elit, sed do eiusmod tempor incididunt ut labore et dolore magna aliquamtis ad minim veniam.</p><a class="more">Continue Reading</a></div>
  <div class="abs post" style="left:432px;top:2220px"><div class="thumb" role="img" aria-label="Photo of an engineer in a server room" style="background:linear-gradient(135deg,#18273d,#3d6a9e)"></div><h4>LOREM IPSUM DOLOR SIT AMET</h4><p>Consectetur adipiscing elit, sed do eiusmod tempor incididunt ut labore et dolore magna aliquamtis ad minim veniam.</p><a class="more">Continue Reading</a></div>
  <div class="abs post" style="left:792px;top:2220px"><div class="thumb" role="img" aria-label="Photo of a hand touching a digital network display" style="background:linear-gradient(135deg,#2f5f94,#9dc2e4)"></div><h4>LOREM IPSUM DOLOR SIT AMET</h4><p>Consectetur adipiscing elit, sed do eiusmod tempor incididunt ut labore et dolore magna aliquamtis ad minim veniam.</p><a class="more">Continue Reading</a></div>

  <!-- news -->
  <h2 class="abs h2" style="top:2670px">NEWS</h2>
  <div class="abs news-main" role="img" aria-label="Illustration of database concept with people and charts"></div>
  <div class="abs news-main-cap">Consectetur adipiscing elit, sed do eiusmod tempor incididunt ut labore et dolore magna aliquamtis.</div>
  <div class="abs news-item" style="top:2740px"><div class="thumb" role="img" aria-label="News photo of server racks"></div><div><h4>LOREM IPSUM DOLOR SIT AMET</h4><p>Consectetur adipiscing elit, sed do eiusmod tempor incididunt ut labore et dolore.</p><a class="more">Read More</a></div></div>
  <div class="abs news-item" style="top:2852px"><div class="thumb" role="img" aria-label="News photo of a data centre"></div><div><h4>LOREM IPSUM DOLOR SIT AMET</h4><p>Consectetur adipiscing elit, sed do eiusmod tempor incididunt ut labore et dolore.</p><a class="more">Read More</a></div></div>
  <div class="abs news-item" style="top:2964px"><div class="thumb" role="img" aria-label="News photo of network equipment"></div><div><h4>LOREM IPSUM DOLOR SIT AMET</h4><p>Consectetur adipiscing elit, sed do eiusmod tempor incididunt ut labore et dolore.</p><a class="more">Read More</a></div></div>

  <!-- testimonial -->
  <div class="abs testi-band"></div>
  <svg class="abs arrow" style="left:80px;top:3300px" viewBox="0 0 30 40" aria-hidden="true"><path d="M22 4 6 20l16 16" fill="none" stroke="#9aa0a8" stroke-width="4"/></svg>
  <svg class="abs arrow" style="left:1090px;top:3300px" viewBox="0 0 30 40" aria-hidden="true"><path d="M8 4l16 16L8 36" fill="none" stroke="#9aa0a8" stroke-width="4"/></svg>
  <div class="abs testi-card">
    <h3>WHAT OUR CLIENT SAYS</h3>
    <blockquote>“ Lorem ipsum dolor sit amet, consectetur adipiscing elit, sed do eiusmod tempor incididunt ut labore et dolore magna aliqua. Ut enim ad minim veniam, quis nostrud exercitation ullamco laboris nisi ut aliquip ex ea commodo consequat. ”</blockquote>
    <div class="testi-avatar" role="img" aria-label="Portrait of the client"></div>
    <div class="name">NAME HEADING</div>
  </div>

  <!-- footer -->
  <footer class="abs footer"></footer>
  <div class="abs f-logo">KOVRILEX</div>
  <div class="abs f-copy">Copyright © 2018 Kovrilex.cz<br>All Rights Reserved.</div>
  <div class="abs f-col" style="left:330px;top:3640px"><h5>SITE MAP</h5><div class="f-grid"><ul><li>Home</li><li>About Us</li><li>Services</li><li>Blog</li></ul><ul><li>Clients</li><li>Solutions</li><li>Contact Us</li></ul></div></div>
  <div class="abs f-col" style="left:560px;top:3640px"><h5>CONTACT US</h5><ul><li>Sales &amp; Support</li><li>Message Us</li><li>Live Chat</li><li>Become A Partner</li></ul></div>
  <div class="abs f-col f-downloads" style="left:740px;top:3640px"><h5>DOWNLOADS</h5><ul>
    <li><svg width="12" height="12" viewBox="0 0 24 24" aria-hidden="true"><path d="M12 3v12m-5-5 5 5 5-5M4 20h16" fill="none" stroke="#5b93e0" stroke-width="3"/></svg>Service Overview (PDF)</li>
    <li><svg width="12" height="12" viewBox="0 0 24 24" aria-hidden="true"><path d="M12 3v12m-5-5 5 5 5-5M4 20h16" fill="none" stroke="#5b93e0" stroke-width="3"/></svg>Company Presentation</li>
    <li><svg width="12" height="12" viewBox="0 0 24 24" aria-hidden="true"><path d="M12 3v12m-5-5 5 5 5-5M4 20h16" fill="none" stroke="#5b93e0" stroke-width="3"/></svg>Training Syllabus</li>
    <li><svg width="12" height="12" viewBox="0 0 24 24" aria-hidden="true"><path d="M12 3v12m-5-5 5 5 5-5M4 20h16" fill="none" stroke="#5b93e0" stroke-width="3"/></svg>DBA Checklist</li>
  </ul></div>
  <div class="abs f-col" style="left:940px;top:3640px"><h5>SUBSCRIBE EMAIL</h5><div class="f-input">Enter Email Address</div><div class="f-btn" style="margin:16px 0 0 94px">Sign Up</div></div>

</div>
</body>
</html>
```